Valduro.com needs a Mobile FIRST Site

Valduro.com is an insurance broker based in Panama City, Panama that plans to sell car and motorcycle insurance online.

We need to design a total of 5 pages (two of those are A/B test pages). The site will be responsive and will be programmed in React. We will be using Brisk Widget´s library to code Valduro.com. Keep in mind that we are using Brisk Widget to program the site´s functions, not to create the "look and feel" of the site, that is obviously your job. You can learn more about Brisk Widget here... https://brisk-widget.example/

We have created wireframes for the app. Please follow and keep in mind the instructions in the wireframes. You can change things here and there as long as the core functions and goals stay intact. We have uploaded the wireframes along with the company logo and color.

We are planning to A/B test the site´s home page so we need to design two homepages. You can find homepage A and B in the wireframes provided.

We speak Spanish in Panama but you can design the site in English. We can change the text once we receive the designs.

Target Market(s)

25-45 year olds who own a car or motorcylcle and own a credit card.

Industry/Entity Type

Insurance

Font styles to use
Sans Serif

Requirements
Must have
• Follow the wireframes provided and the logo colors.
Nice to have
• Please look at the Image I´ve uploaded from DeskHaven, use it as reference to create HomePage A.

```html
<!DOCTYPE html>
<html lang="es">
<head>
<meta charset="utf-8">
<title>Valduro.com — Claim aquí</title>
<link rel="stylesheet" href="https://fonts.googleapis.com/css2?family=Roboto:wght@400;500;700&family=Lato:wght@400;700;900&display=swap">
<style>
:root{
  --purple:#2a1466;
  --black:#161616;
  --page:#efefef;
  --white:#ffffff;
  --line:#c9c9c9;
  --text:#333333;
  --muted:#4a4a4a;
  --star:#f5c518;
}
*{box-sizing:border-box;margin:0;padding:0}
html,body{width:1200px;height:2536px;overflow:hidden;background:var(--page)}
body{font-family:'Roboto',sans-serif;color:var(--text)}
.stage{position:absolute;left:0;top:0;width:414px;height:875px;transform:scale(2.8986);transform-origin:0 0;background:var(--page)}
.abs{position:absolute}
.header{left:0;top:0;width:414px;height:48px;background:var(--white)}
.logo{left:0;width:414px;top:12px;text-align:center;font-family:'Lato',sans-serif;font-weight:900;font-size:21px;color:var(--purple);letter-spacing:-.3px}
.title{left:0;width:414px;top:70px;text-align:center;font-family:'Lato',sans-serif;font-size:19px;letter-spacing:.5px;color:#222}
.intro{left:28px;width:358px;top:111px;text-align:center;font-size:12.5px;line-height:23px;color:var(--muted)}
.step{height:27px;border-radius:4px;font-size:13px;line-height:25px;text-align:center;border:1.5px solid var(--purple);color:#333;background:var(--white)}
.step.active{background:var(--black);border-color:var(--black);color:var(--white)}
.dots{height:0;border-top:1.5px dotted var(--purple)}
.tab{top:235px;height:40px;display:flex;align-items:center;justify-content:center;gap:12px;font-family:'Lato',sans-serif;font-size:15px;border:1.5px solid var(--black)}
.tab.on{background:var(--purple);color:var(--white);border-color:var(--purple)}
.tab.off{background:var(--white);color:var(--purple)}
.panel{left:33px;top:280px;width:348px;height:553px;background:var(--white);border:1px solid var(--line)}
.plan-alt{left:208px;top:288px;width:165px;height:541px;background:#f4f4f4;border:1.5px solid var(--line)}
.photo{border-radius:40%}
.price{text-align:center;font-size:13.5px;color:#222}
.rule{height:1px;background:#999}
.label{font-size:10px;line-height:16px;color:#333}
.bar{height:19px;width:130px;border:1px solid var(--line);background:var(--white)}
.bar span{display:block;height:100%;width:80%;background:var(--purple);color:var(--white);font-size:8.5px;line-height:17px;padding-left:7px}
.benefits-title{font-family:'Lato',sans-serif;font-weight:700;font-size:11.5px;color:#111}
.benefits{list-style:none;font-size:10.5px;color:#333}
.benefits li{height:21px;position:relative;padding-left:18px}
.benefits li::before{content:"";position:absolute;left:0;top:4px;width:6px;height:6px;border-radius:50%;background:var(--purple)}
.buy{height:26px;border-radius:4px;background:var(--black);color:var(--white);font-size:12px;line-height:26px;text-align:center}
.footer{left:0;top:850px;width:414px;height:25px;background:var(--black);color:var(--white);font-size:9px;line-height:25px;text-align:center}
</style>
</head>
<body>
<div class="stage">
  <header class="abs header">
    <svg class="abs" style="left:16px;top:17px" width="14" height="12" viewBox="0 0 14 12"><rect width="14" height="2.4" fill="#666"/><rect y="4.8" width="14" height="2.4" fill="#666"/><rect y="9.6" width="14" height="2.4" fill="#666"/></svg>
    <div class="abs logo">Valduro.com</div>
    <svg class="abs" style="left:380px;top:16px" width="15" height="15" viewBox="0 0 15 15"><circle cx="6" cy="6" r="4.6" fill="none" stroke="#666" stroke-width="2.2"/><line x1="9.5" y1="9.5" x2="14" y2="14" stroke="#666" stroke-width="2.6" stroke-linecap="round"/></svg>
  </header>

  <h1 class="abs title">CLAIM AQUÍ</h1>
  <p class="abs intro">Lorem ipsum dolor sit amet, consectetur adipiscing elit, sed do eiusmod tempor incididunt ut labore et dolore.</p>

  <div class="abs step active" style="left:44px;top:180px;width:77px">1. Elige</div>
  <div class="abs dots" style="left:121px;top:193px;width:48px"></div>
  <div class="abs step" style="left:169px;top:180px;width:78px">2. Datos</div>
  <div class="abs dots" style="left:247px;top:193px;width:47px"></div>
  <div class="abs step" style="left:294px;top:180px;width:76px">3. Paga</div>

  <div class="abs tab on" style="left:33px;width:175px">
    <svg width="20" height="14" viewBox="0 0 20 14"><path d="M2 7 L4.5 1.5 H15.5 L18 7 V12 H2 Z" fill="#fff"/><rect x="5.5" y="3" width="9" height="3.5" fill="#2a1466"/><circle cx="5.5" cy="9.5" r="1.5" fill="#2a1466"/><circle cx="14.5" cy="9.5" r="1.5" fill="#2a1466"/></svg>
    <span>CARROS</span>
  </div>
  <div class="abs tab off" style="left:207px;width:174px">
    <svg width="24" height="14" viewBox="0 0 24 14"><circle cx="5" cy="9" r="4" fill="none" stroke="#2a1466" stroke-width="2"/><circle cx="19" cy="9" r="4" fill="none" stroke="#2a1466" stroke-width="2"/><path d="M5 9 L10 4 H15 L19 9 M10 4 L12 9 H15" fill="none" stroke="#2a1466" stroke-width="2"/></svg>
    <span>MOTOS</span>
  </div>

  <section class="abs panel"></section>

  <!-- featured plan -->
  <svg class="abs" style="left:152px;top:285px" width="51" height="45" viewBox="0 0 51 45"><path d="M0 0 H51 V45 A51 45 0 0 1 0 0 Z" fill="#2a1466"/><polygon points="27,7 30.5,15.5 39.5,16 32.5,22 35,31 27,26 19,31 21.5,22 14.5,16 23.5,15.5" fill="#f5c518" stroke="#c89400" stroke-width=".8"/></svg>
  <div class="abs photo" role="img" aria-label="Red hatchback car" style="left:52px;top:318px;width:134px;height:72px;background:radial-gradient(ellipse at 50% 45%,#e2252b 0%,#b5141a 55%,#e8e8e8 100%)"></div>
  <div class="abs price" style="left:34px;width:170px;top:430px">$150,00</div>
  <div class="abs rule" style="left:52px;top:455px;width:134px"></div>
  <div class="abs label" style="left:50px;top:474px">Insurance coverage</div>
  <div class="abs bar" style="left:50px;top:491px"><span>$10,000</span></div>
  <div class="abs label" style="left:50px;top:531px">Insurance coverage<br>limit by accident</div>
  <div class="abs bar" style="left:50px;top:566px"><span>$15,000</span></div>
  <div class="abs label" style="left:50px;top:606px">Insurance coverage<br>by year</div>
  <div class="abs bar" style="left:50px;top:642px"><span>$10,000</span></div>
  <div class="abs rule" style="left:52px;top:688px;width:134px"></div>
  <div class="abs benefits-title" style="left:51px;top:703px">BENEFICIOS</div>
  <ul class="abs benefits" style="left:52px;top:729px"><li>Excepteur</li><li>Doloremque</li><li>Voluptate</li></ul>
  <div class="abs buy" style="left:52px;top:799px;width:101px">COMPRAR</div>

  <!-- second plan -->
  <section class="abs plan-alt"></section>
  <div class="abs photo" role="img" aria-label="Orange hatchback car with reflection" style="left:237px;top:318px;width:95px;height:88px;background:radial-gradient(ellipse at 50% 35%,#f07a1a 0%,#e2641a 45%,#f4f4f4 100%)"></div>
  <div class="abs price" style="left:209px;width:164px;top:433px">$120,00</div>
  <div class="abs rule" style="left:228px;top:459px;width:126px"></div>
  <div class="abs label" style="left:227px;top:478px">Insurance coverage</div>
  <div class="abs bar" style="left:227px;top:494px;width:126px"><span>$10,000</span></div>
  <div class="abs label" style="left:227px;top:533px">Insurance coverage<br>limit by accident</div>
  <div class="abs bar" style="left:227px;top:567px;width:126px"><span>$15,000</span></div>
  <div class="abs label" style="left:227px;top:605px">Insurance coverage<br>by year</div>
  <div class="abs bar" style="left:227px;top:641px;width:126px"><span>$10,000</span></div>
  <div class="abs rule" style="left:228px;top:684px;width:126px"></div>
  <div class="abs benefits-title" style="left:228px;top:698px">BENEFICIOS</div>
  <ul class="abs benefits" style="left:228px;top:724px"><li>Excepteur</li><li>Doloremque</li><li>Voluptate</li></ul>
  <div class="abs buy" style="left:228px;top:793px;width:98px">COMPRAR</div>

  <footer class="abs footer">©Copyrights2018VALDURO..All Rights Reserved</footer>
</div>
</body>
</html>
```